Fern Assembly Business Cards

Looking or a business card design for my start-up, called "Fern Assembly".
Our tagline is "Unleashing the human potential for good through leadership, culture, and education."
Our mission-driven work includes professional/personal development workshops, educational design services, organizational & project management consulting, and coaching services for K-12 schools, organizations, and individuals.
You can check out the website we're building at fernassembly.example
I select projects from designers who are highly responsive to feedback, engage in dialog about revisions, and provide all root/source documents (so please state in your initial submission that you agree to do so).
Looking forward to seeing your great designs!!
Updates
Hello everyone,
Industry/Entity Type
Building
Requirements
Must have
- Looking for a two sided design that includes our logo (I am uploading two variations that I would like incorporated in .ai format) and website on both sides.
The front side must include:
Logo, Name, Title, Phone, Email, Twitter handle
The back side must include: Logo, @fernassem (our organizational twitter handle)
Nice to have
- I like the rounded corner business cards, but that is not absolutely essential.
Should not have
- Colors beyond those presented in our logo.

```html
<!DOCTYPE html>
<html lang="en">
<head>
<meta charset="utf-8">
<title>Fern Assembly – Business Cards</title>
<link rel="stylesheet" href="https://fonts.googleapis.com/css2?family=Cormorant+Garamond:wght@500&family=Open+Sans:wght@700&display=swap">
<style>
  :root {
    --page: #e6e6e6;
    --card: #050505;
    --card-edge: #1a1a1a;
    --sky: #7ccbe3;
    --accent: #1d84c6;
    --text: #d2d2d2;
    --muted: #8d8d8d;
  }
  * { box-sizing: border-box; margin: 0; padding: 0; }
  html, body {
    width: 1200px; height: 911px; overflow: hidden;
    background: var(--page);
  }
  .sheet { position: relative; width: 1200px; height: 911px; }
  .card {
    position: absolute; top: 293px;
    width: 566px; height: 324px;
    background: var(--card);
    border: 1px solid var(--card-edge);
    border-radius: 14px;
    overflow: hidden;
  }
  .card--front { left: 22px; }
  .card--back { left: 610px; width: 560px; }

  .brand {
    position: absolute;
    display: flex; flex-direction: column; align-items: center;
    text-align: center;
  }
  .brand__mark {
    width: 70px; height: 70px; border-radius: 50%;
    background: var(--sky); margin-bottom: 12px;
  }
  .brand__name {
    font-family: "Cormorant Garamond", serif;
    font-weight: 500; font-size: 21px; letter-spacing: 0.5px;
    text-transform: uppercase; color: var(--text); white-space: nowrap;
  }
  .brand__tagline {
    font-family: "Cormorant Garamond", serif;
    font-size: 7px; letter-spacing: 2.6px; text-transform: uppercase;
    color: var(--muted); margin-top: 2px; white-space: nowrap;
  }
  .brand__web {
    font-family: "Cormorant Garamond", serif;
    font-size: 6px; color: var(--muted); margin-top: 5px;
  }
  .card--front .brand { left: 0; width: 285px; top: 100px; }
  .card--back .brand { left: 0; width: 100%; top: 58px; }

  .divider {
    position: absolute; left: 284px; top: 26px;
    width: 2px; height: 272px;
    background: linear-gradient(to bottom, transparent, var(--accent) 20%, var(--accent) 80%, transparent);
  }
  .contacts {
    position: absolute; left: 316px; top: 96px;
    list-style: none;
  }
  .contact {
    display: flex; align-items: center; gap: 13px;
    height: 37px;
    font-family: "Open Sans", sans-serif; font-weight: 700;
    font-size: 14.5px; color: var(--text);
  }
  .contact__icon { width: 22px; height: 22px; flex: none; }
  .contact__dot {
    width: 18px; height: 18px; border-radius: 50%;
    background: var(--sky); margin: 0 2px; flex: none;
  }
  .handle {
    position: absolute; left: 0; width: 100%; top: 210px;
    display: flex; justify-content: center; align-items: center; gap: 8px;
    font-family: "Open Sans", sans-serif; font-weight: 700;
    font-size: 14.5px; color: var(--text);
  }
  .glow-line {
    position: absolute; left: 20px; right: 20px; top: 269px; height: 3px;
    background: linear-gradient(to right, transparent, var(--accent) 40%, var(--accent) 60%, transparent);
    opacity: 0.8;
  }
</style>
</head>
<body>
<main class="sheet">
  <section class="card card--front" aria-label="Business card front">
    <div class="brand">
      <span class="brand__mark"></span>
      <span class="brand__name">Fern Assembly</span>
      <span class="brand__tagline">Leadership | Culture | Education</span>
      <span class="brand__web">www.fernassembly.example</span>
    </div>
    <span class="divider"></span>
    <ul class="contacts">
      <li class="contact">
        <svg class="contact__icon" viewBox="0 0 22 22"><rect x="6" y="1.5" width="10" height="19" rx="2" fill="none" stroke="var(--sky)" stroke-width="1.8"/><rect x="8" y="4" width="6" height="11" fill="var(--sky)"/><circle cx="11" cy="17.7" r="1" fill="var(--sky)"/></svg>
        <span>555010 284</span>
      </li>
      <li class="contact">
        <svg class="contact__icon" viewBox="0 0 22 22"><rect x="1.5" y="5" width="19" height="13" fill="none" stroke="var(--sky)" stroke-width="1.8"/><path d="M1.5 5 L11 13 L20.5 5 M1.5 18 L8 11.5 M20.5 18 L14 11.5" fill="none" stroke="var(--sky)" stroke-width="1.6"/></svg>
        <span>fernassem@fern</span>
      </li>
      <li class="contact">
        <span class="contact__dot"></span>
        <span>@fernassem</span>
      </li>
      <li class="contact">
        <svg class="contact__icon" viewBox="0 0 22 22"><text x="11" y="17" text-anchor="middle" font-family="Open Sans, sans-serif" font-weight="700" font-size="18" fill="var(--sky)">@</text></svg>
        <span>www.fernassembly.example</span>
      </li>
    </ul>
  </section>

  <section class="card card--back" aria-label="Business card back">
    <div class="brand">
      <span class="brand__mark"></span>
      <span class="brand__name">Fern Assembly</span>
      <span class="brand__tagline">Leadership | Culture | Education</span>
      <span class="brand__web">www.fernassembly.example</span>
    </div>
    <div class="handle">
      <span class="contact__dot"></span>
      <span>@fernassem</span>
    </div>
    <span class="glow-line"></span>
  </section>
</main>
</body>
</html>
```